Business Card for Multi-Brand Sportswear Company

We are looking for a business card which represents our company and the multiple brands within it.

The company: Kelt Athletic (LTD)
The brands: Kelt, PawaLuni, VerdantFlex, Grit and Gale

Employees using these cards would be representing Kelt Athletic, rather than any of the individual brands. You will see a current design within the uploaded files, to give some inspiration. The actual text of the brands is not necessary, but the logos should be on there is some format.

Our creative minds on this are stretched, so we are looking for someone to make this their own, and show us what a good business card should look like.

We may like to get these printed with spot gloss, so keep that in mind with your designs.

www.keltathletic.co.uk

Industry/Entity Type

Business

Contact Information for Business Card

Tom Hollingsworth-Pryce
Operations Manager
(+44) 1632 960 418
Tom@keltathletic.co.uk
www.keltathletic.co.uk

Font styles to use
Sans Serif
Other font styles liked:
• Eurostile

Colors
ffffff

Requirements
Nice to have
• Dark (black) background

```html
<!DOCTYPE html>
<html lang="en">
<head>
<meta charset="utf-8">
<title>Kelt Athletic – Business Card</title>
<link rel="stylesheet" href="https://fonts.googleapis.com/css2?family=Quicksand:wght@500;600;700&family=Saira:wght@400;500&display=swap">
<style>
  :root {
    --backdrop: #808080;
    --card: #212121;
    --ink: #ffffff;
    --accent: #d71f26;
    --plum: #5e4d66;
    --plum-text: #c9bcd1;
    --stone: #9a9a9a;
  }
  * { box-sizing: border-box; margin: 0; padding: 0; }
  html, body {
    width: 1200px; height: 854px; overflow: hidden;
    background: var(--backdrop);
  }
  .sheet { position: relative; width: 1200px; height: 854px; }
  .card {
    position: absolute; top: 264px;
    width: 512px; height: 292px;
    background: var(--card);
    overflow: hidden;
    color: var(--ink);
  }
  .card--front { left: 78px; }
  .card--back { left: 609px; }
  .card .slash { position: absolute; inset: 0; }

  .wordmark { position: absolute; font-family: "Saira", sans-serif; }
  .wordmark__name { font-weight: 500; color: var(--ink); letter-spacing: 0.02em; white-space: nowrap; line-height: 1; }
  .wordmark__tag { font-weight: 400; color: var(--ink); letter-spacing: 0.2em; text-align: right; line-height: 1; }

  .card--front .wordmark { left: 38px; top: 124px; width: 192px; }
  .card--front .wordmark__name { font-size: 25px; }
  .card--front .wordmark__tag { font-size: 5px; margin-top: 3px; }
  .card--back .wordmark { left: 72px; top: 86px; width: 372px; }
  .card--back .wordmark__name { font-size: 48px; }
  .card--back .wordmark__tag { font-size: 10px; margin-top: 6px; }

  .brands { position: absolute; display: flex; align-items: center; font-family: "Saira", sans-serif; font-weight: 500; }
  .brand { white-space: nowrap; line-height: 1; }
  .brand--pawaluni { color: var(--plum-text); }
  .brand--grit { color: var(--accent); }
  .brand--kelt { color: var(--ink); }
  .brand--verdant { color: var(--stone); }
  .card--front .brands { left: 58px; top: 178px; gap: 8px; font-size: 7px; }
  .card--back .brands { right: 26px; top: 245px; gap: 14px; font-size: 12px; }

  .person { position: absolute; right: 28px; top: 116px; text-align: right; font-family: "Quicksand", sans-serif; }
  .person__name { font-weight: 700; font-size: 19px; letter-spacing: -0.01em; }
  .person__role { font-weight: 500; font-size: 15px; margin-top: 10px; }

  .contacts { position: absolute; left: 311px; top: 196px; list-style: none; font-family: "Quicksand", sans-serif; font-weight: 500; font-size: 13.5px; }
  .contacts li { display: flex; align-items: center; gap: 9px; height: 24px; }
  .contacts svg { width: 13px; height: 13px; flex: none; }
</style>
</head>
<body>
<main class="sheet">

  <section class="card card--front" aria-label="Business card front">
    <svg class="slash" width="512" height="292" viewBox="0 0 512 292" aria-hidden="true">
      <line x1="365" y1="0" x2="130" y2="292" stroke="var(--accent)" stroke-width="1.6"/>
    </svg>

    <div class="wordmark">
      <p class="wordmark__name">KELT ATHLETIC</p>
      <p class="wordmark__tag">PERFORMANCE WEAR</p>
    </div>

    <div class="brands" aria-label="Brands">
      <span class="brand brand--pawaluni">PawaLuni</span>
      <span class="brand brand--grit">Grit and Gale</span>
      <span class="brand brand--kelt">Kelt</span>
      <span class="brand brand--verdant">VerdantFlex</span>
    </div>

    <div class="person">
      <p class="person__name">Tom Hollingsworth-Pryce</p>
      <p class="person__role">Operations Manager</p>
    </div>

    <ul class="contacts">
      <li>
        <svg viewBox="0 0 16 16" aria-hidden="true"><path d="M4 1.5 6 4.5 4.8 6c.8 2 2.5 3.7 4.6 4.7L11 9.5l3 2-1.2 2.3C8 13.5 2.5 8 2.2 3.2Z" fill="none" stroke="var(--ink)" stroke-width="1.3" stroke-linejoin="round"/></svg>
        <span>(+44) 1632 960 418</span>
      </li>
      <li>
        <svg viewBox="0 0 16 16" aria-hidden="true"><rect x="1.5" y="3.5" width="13" height="9" fill="none" stroke="var(--ink)" stroke-width="1.3"/><path d="M1.5 3.5 8 9l6.5-5.5" fill="none" stroke="var(--ink)" stroke-width="1.3"/></svg>
        <span>Tom@keltathletic.co.uk</span>
      </li>
      <li>
        <svg viewBox="0 0 16 16" aria-hidden="true"><g fill="none" stroke="var(--ink)" stroke-width="1.1"><circle cx="8" cy="8" r="6.5"/><ellipse cx="8" cy="8" rx="2.8" ry="6.5"/><path d="M1.5 8h13M2.5 4.7h11M2.5 11.3h11"/></g></svg>
        <span>www.keltathletic.co.uk</span>
      </li>
    </ul>
  </section>

  <section class="card card--back" aria-label="Business card back">
    <svg class="slash" width="512" height="292" viewBox="0 0 512 292" aria-hidden="true">
      <line x1="0" y1="249" x2="512" y2="137" stroke="var(--accent)" stroke-width="1.8"/>
    </svg>

    <div class="wordmark">
      <p class="wordmark__name">KELT ATHLETIC</p>
      <p class="wordmark__tag">PERFORMANCE WEAR</p>
    </div>

    <div class="brands" aria-label="Brands">
      <span class="brand brand--pawaluni">PawaLuni</span>
      <span class="brand brand--grit">Grit and Gale</span>
      <span class="brand brand--kelt">Kelt</span>
      <span class="brand brand--verdant">VerdantFlex</span>
    </div>
  </section>

</main>
</body>
</html>
```